General Contractor Website Design

We are working with a General Contractor in California that specializes in building custom kitchens, baths, and homes for high-end clients.

Here are some websites for inspiration:
https://morvelstudio.example/
https://ridgelanebuildworks.example
https://www.framequill.example
https://www.nestiva.example
https://www.tzdwell.example
https://rplresidences.example

Thank you for taking the time to consider designing a website for us. We are web developers based in Stockton, CA, USA. Most of our projects go through the same process. Understanding this process may help you win a project with us. We custom-code all of our websites in-house. We don’t have any requirements as to what tools you use for your design, but we ask that you follow these guidelines.

IMAGES:
If you use any images or icons in the design, we ask that you have a link to the asset so we can purchase the image/icon. Most of the designs we submit do not have the customer’s images on them unless they have some great images. Be creative; show us the feeling you are trying to portray with your image choices. Use any royalty-free site you choose. We subscribe to Velqor and mainly use their images, but we can purchase images outside of Velqor. PLEASE NOTE: we will not submit designs to clients with watermarks on the images.

FONTS:
We ask that you identify the fonts you’re using in the design. This can be done in a message if you want. We typically use Google Fonts and Velqor Fonts.

CONTENT:
We're always open to different content and ideas. We often submit designs with stock images so the client can see our vision. We typically take pictures after the website launch to use their images with our vision. Lorem Ipsum is fine for paragraphs, but we ask that you make the Headers with correct English. We want to be able to show the vision and identify the sections of the website.

INSPIRATION:
We typically add a couple of links in the brief of websites we like to help you get started in your design.

REVISIONS:
We do not often ask for revisions of the designs unless we see something in the design that may not appeal to the client. If there are slight changes that we want to make, we do that in the development process.

FEEDBACK:
We rarely give feedback on designs during the design process. We are working on many website projects and do not have the time to provide feedback. We usually respond if your request is well thought out and asks specific questions, but a note asking “feedback, please” usually goes unanswered.

```html
<!DOCTYPE html>
<html lang="en">
<head>
<meta charset="utf-8">
<title>Hollowmere Builders — General Contractor</title>
<link rel="stylesheet" href="https://fonts.googleapis.com/css2?family=Poppins:wght@300;400;500;600;700;800&display=swap">
<style>
:root{
  --red:#e31d2f;
  --black:#000;
  --white:#fff;
  --ink:#222;
  --muted:#777;
  --soft:#f2f2f2;
  --card-grey:#c4c4c4;
  --name-grey:#8a8a8a;
}
*{margin:0;padding:0;box-sizing:border-box}
html,body{width:1200px;height:4796px;overflow:hidden}
body{font-family:"Poppins",sans-serif;color:var(--ink);background:var(--white);position:relative}
.abs{position:absolute}
a{color:inherit;text-decoration:none}

/* top bar */
.topbar{top:0;left:0;width:1200px;height:43px;background:var(--red);color:var(--white);font-size:15px}
.topbar .item{top:11px;display:flex;align-items:center;gap:10px}
.brand{font-weight:600;letter-spacing:4px;line-height:1.05;text-transform:uppercase;display:flex;align-items:center;gap:10px}
.brand .mark{width:34px;height:34px;background:var(--red)}

/* header */
.header{top:43px;left:0;width:1200px;height:119px;background:var(--white)}
.header .brand{left:87px;top:40px;color:var(--ink);font-size:18px}
.nav{right:87px;top:44px;display:flex;gap:38px;font-size:15px}
.nav a{position:relative;padding-bottom:12px}
.nav a.active{color:var(--red)}
.nav a.active::after{content:"";position:absolute;left:-6px;right:-6px;bottom:0;height:2px;background:var(--red)}

/* hero */
.hero{top:162px;left:0;width:1200px;height:642px;background:linear-gradient(90deg,#3d3d3f 0%,#5a5856 45%,#7c7874 75%,#8e8a86 100%)}
.hero h1{top:138px;left:0;width:1200px;text-align:center;color:var(--white);font-size:40px;font-weight:700;line-height:52px;text-transform:uppercase}
.hero p{top:270px;left:260px;width:680px;text-align:center;color:var(--white);font-size:15px;line-height:25px}
.btn{display:flex;align-items:center;justify-content:center;font-weight:500}
.hero .btn{top:359px;left:502px;width:196px;height:72px;background:var(--red);color:var(--white);font-size:20px}
.dots{display:flex;gap:6px}
.dots span{width:14px;height:14px;border-radius:50%;background:#cfcfcf}
.hero .dots{top:514px;left:563px}
.hero .dots span:first-child{background:var(--white)}
.hero-edge{left:0;bottom:0}

/* services */
.services{top:804px;left:0;width:1200px;height:703px;background:var(--soft)}
.section-title{left:0;width:1200px;text-align:center;font-size:30px;font-weight:700;text-transform:uppercase;color:var(--ink)}
.section-title em{font-style:normal;color:var(--red)}
.card{top:186px;width:326px;height:411px;background:var(--white);text-align:center}
.card .photo{position:relative;height:186px;background:linear-gradient(180deg,#e9e9e7,#c8c4bd 60%,#8d8277)}
.card .photo svg{position:absolute;left:0;bottom:0}
.card h3{margin-top:18px;color:var(--red);font-size:20px;font-weight:500;text-transform:uppercase}
.card p{margin:14px auto 0;width:280px;font-size:14px;line-height:26px;color:var(--muted)}
.card .btn{margin:20px auto 0;width:114px;height:43px;background:var(--red);color:var(--white);font-size:13px}

/* about */
.about{top:1507px;left:0;width:1200px;height:586px;background:var(--red);color:var(--white)}
.about h2{top:80px;left:87px;display:flex;align-items:center;gap:18px;font-size:30px;font-weight:700}
.about h2 .brand{font-size:22px;font-weight:300;letter-spacing:5px}
.about p{top:155px;left:87px;width:500px;font-size:15px;line-height:31px}
.about .btn{top:441px;left:87px;width:160px;height:48px;background:var(--white);color:var(--red);font-size:15px}
.about .frame{top:74px;left:655px}

/* portfolio */
.portfolio{top:2093px;left:0;width:1200px;height:1289px;background:var(--white)}
.cat{left:87px;font-size:20px;font-weight:600;text-transform:uppercase}
.cat.red{color:var(--red)}
.shot{width:326px;height:211px}
.view{width:135px;height:51px;left:978px;font-size:15px;color:var(--white)}
.view.dark{background:var(--black)}
.view.red{background:var(--red)}

/* testimonials */
.testimonials{top:3382px;left:0;width:1200px;height:925px;background:var(--black)}
.testimonials .section-title{color:var(--white);top:112px}
.quote{background:var(--card-grey);color:#888;text-align:center;font-size:15px;line-height:26px;padding:28px 18px 0}
.quote.main{background:var(--white);color:#555;font-size:16px;line-height:26px;padding:38px 24px 0;text-align:justify;text-align-last:center}
.avatar{border-radius:50%;background:radial-gradient(circle at 50% 40%,#d9d9d9,#8c8c8c);border:3px solid #eee}
.who{text-align:center;color:var(--name-grey);font-size:16px;line-height:22px}
.who small{display:block;font-size:13px}
.who.main{color:var(--white);font-size:20px;font-weight:500;line-height:30px}
.who.main small{font-size:14px;font-weight:400}
.testimonials .dots{top:818px;left:553px}
.testimonials .dots span:nth-child(2){background:var(--red)}

/* footer */
.footer{top:4307px;left:0;width:1200px;height:489px;background:var(--red);color:var(--white)}
.footer .brand.foot{left:0;width:1200px;justify-content:center;top:70px;font-size:28px;font-weight:300;letter-spacing:6px}
.footer .brand.foot .mark{background:var(--white);width:40px;height:40px}
.footer h4{font-size:24px;font-weight:600;text-transform:uppercase}
.footer .col{top:190px}
.footer .col p{margin-top:12px;font-size:15px;line-height:26px}
.social{display:flex;gap:6px;margin-top:28px}
.social span{width:22px;height:22px;border:1.5px solid var(--white);border-radius:50%}
.contact-row{display:flex;align-items:center;gap:18px;margin-top:16px;font-size:15px}
.contact-row .ic{width:32px;height:32px;border-radius:50%;background:var(--white);display:flex;align-items:center;justify-content:center;flex:none}
.links a{display:block;font-size:15px;line-height:26px;margin-left:4px}
.footer .rule{top:412px;left:87px;width:1026px;height:1px;background:rgba(255,255,255,.45)}
.copyright{top:438px;left:0;width:1200px;text-align:center;font-size:13px}
</style>
</head>
<body>

<div class="abs topbar">
  <div class="abs item" style="left:734px">
    <svg width="28" height="20" viewBox="0 0 28 20"><rect x="1" y="1" width="26" height="18" fill="none" stroke="#fff" stroke-width="2"/><path d="M1 1 L14 11 L27 1" fill="none" stroke="#fff" stroke-width="2"/></svg>
    <span>info@websitename.com</span>
  </div>
  <div class="abs item" style="left:984px">
    <svg width="22" height="22" viewBox="0 0 24 24"><path d="M6.6 10.8c1.4 2.8 3.8 5.1 6.6 6.6l2.2-2.2c.3-.3.7-.4 1-.2 1.1.4 2.3.6 3.6.6.6 0 1 .4 1 1V20c0 .6-.4 1-1 1C10.6 21 3 13.4 3 4c0-.6.4-1 1-1h3.5c.6 0 1 .4 1 1 0 1.3.2 2.5.6 3.6.1.3 0 .7-.2 1z" fill="#fff"/></svg>
    <span>+0123456789</span>
  </div>
</div>

<header class="abs header">
  <div class="abs brand"><span class="mark"></span><span>Hollowmere<br>Builders</span></div>
  <nav class="abs nav">
    <a class="active" href="#">Home</a><a href="#">About Us</a><a href="#">Services</a><a href="#">Portfolio</a><a href="#">Testimonials</a><a href="#">Contact Us</a>
  </nav>
</header>

<section class="abs hero" role="img" aria-label="Modern living room with grey sofa, spiral staircase and stone wall">
  <h1 class="abs">Praesent suscipit consectetur<br>magna a vestibulum</h1>
  <p class="abs">Lorem ipsum is placeholder text commonly used in the graphic, print, and publishing industries for previewing layouts and visual mockups.</p>
  <a class="abs btn" href="#">Read More</a>
  <div class="abs dots"><span></span><span></span><span></span><span></span></div>
  <svg class="abs hero-edge" width="1200" height="110" viewBox="0 0 1200 110">
    <polygon points="0,110 0,60 540,32 1200,78 1200,110" fill="#f2f2f2"/>
    <polygon points="0,96 0,60 540,32 560,36 0,110" fill="#e31d2f"/>
  </svg>
</section>

<section class="abs services">
  <h2 class="abs section-title" style="top:88px">Our <em>Services</em></h2>
  <article class="abs card" style="left:87px">
    <div class="photo" role="img" aria-label="Bright white kitchen with island and pendant lights"><svg width="326" height="30" viewBox="0 0 326 30"><polygon points="0,30 0,24 60,0 326,18 326,30" fill="#fff"/><polygon points="0,24 60,0 326,18 326,24 60,6 0,30" fill="#e31d2f"/></svg></div>
    <h3>Kitchen Designs</h3>
    <p>Lorem ipsum dolor sit amet, slit consectetur adipiscing elit. Nulla de sit ultricies efficitur orci nec sagittis</p>
    <a class="btn" href="#">Read More</a>
  </article>
  <article class="abs card" style="left:439px">
    <div class="photo" role="img" aria-label="Bright white kitchen with island and pendant lights"><svg width="326" height="30" viewBox="0 0 326 30"><polygon points="0,30 0,24 60,0 326,18 326,30" fill="#fff"/><polygon points="0,24 60,0 326,18 326,24 60,6 0,30" fill="#e31d2f"/></svg></div>
    <h3>Bathrooms Designs</h3>
    <p>Lorem ipsum dolor sit amet, slit consectetur adipiscing elit. Nulla de sit ultricies efficitur orci nec sagittis</p>
    <a class="btn" href="#">Read More</a>
  </article>
  <article class="abs card" style="left:791px">
    <div class="photo" role="img" aria-label="Bright white kitchen with island and pendant lights"><svg width="326" height="30" viewBox="0 0 326 30"><polygon points="0,30 0,24 60,0 326,18 326,30" fill="#fff"/><polygon points="0,24 60,0 326,18 326,24 60,6 0,30" fill="#e31d2f"/></svg></div>
    <h3>Home Designs</h3>
    <p>Lorem ipsum dolor sit amet, slit consectetur adipiscing elit. Nulla de sit ultricies efficitur orci nec sagittis</p>
    <a class="btn" href="#">Read More</a>
  </article>
</section>

<section class="abs about">
  <h2 class="abs">ABOUT <span class="brand">Hollowmere<br>Builders</span></h2>
  <p class="abs">Lorem ipsum dolor sit amet, consectetur adipiscing elit, sed do eiusmod tempor incididunt ut labore et dolore magna aliqua. Ut enim ad minim veniam, quis nostrud exercitation ullamco laboris nisi ut aliquip ex ea commodo consequat. Duis aute irure dolor in reprehenderit in voluptate velit esse cillum dolore eu fugiat nulla pariatur. Excepteur sint occaecat cupidatat non proident, sunt in culpa qui officia deserunt mollit anim id est laborum.</p>
  <a class="abs btn" href="#">Read More</a>
  <svg class="abs frame" width="460" height="452" viewBox="0 0 460 452">
    <polygon points="0,6 120,0 200,28 460,0 460,452 340,436 260,446 0,452" fill="#111"/>
    <foreignObject x="6" y="10" width="448" height="432">
      <div role="img" aria-label="Construction engineer in hard hat and safety vest holding a clipboard on a building site" style="width:448px;height:432px;background:linear-gradient(135deg,#d9a84a,#c9b88a 40%,#9fbfd6 70%,#d7d0bb)"></div>
    </foreignObject>
    <polygon points="6,10 120,6 200,34 454,6 454,0 200,28 120,0 0,6 0,452 60,452 6,420" fill="#111"/>
  </svg>
</section>

<section class="abs portfolio">
  <h2 class="abs section-title" style="top:96px">Our <em>Portfolio</em></h2>

  <h3 class="abs cat" style="top:160px">Kitchens</h3>
  <div class="abs shot" style="left:87px;top:204px;background:linear-gradient(135deg,#c9ccd0,#a8875f 60%,#5c5048)" role="img" aria-label="Modern kitchen with wood cabinets and marble island"></div>
  <div class="abs shot" style="left:437px;top:204px;background:linear-gradient(180deg,#f0f0ee,#d8d6d1 55%,#8e8276)" role="img" aria-label="White kitchen with island and bar stools"></div>
  <div class="abs shot" style="left:787px;top:204px;background:linear-gradient(135deg,#d9cbb6,#b49a80 55%,#6c5a4c)" role="img" aria-label="Narrow kitchen with patterned tile floor"></div>
  <a class="abs btn view dark" style="top:441px" href="#">View More</a>

  <h3 class="abs cat red" style="top:517px">Bathrooms</h3>
  <div class="abs shot" style="left:87px;top:560px;background:linear-gradient(135deg,#3e5a45,#a86c3a 45%,#2a2f3a)" role="img" aria-label="Bathroom with stone bathtub and wood panel wall"></div>
  <div class="abs shot" style="left:437px;top:560px;background:linear-gradient(90deg,#b8874f,#e2dcd3 45%,#3a332e)" role="img" aria-label="Bathroom with wood wall and glass shower"></div>
  <div class="abs shot" style="left:787px;top:560px;background:linear-gradient(135deg,#e6e2dc,#c8ccd0 55%,#9aa4ad)" role="img" aria-label="White bathroom with round mirror and tiled shower"></div>
  <a class="abs btn view red" style="top:798px" href="#">View More</a>

  <h3 class="abs cat" style="top:876px">Homes</h3>
  <div class="abs shot" style="left:87px;top:920px;background:linear-gradient(180deg,#7b84a8,#c79a88 40%,#4a4d58 80%)" role="img" aria-label="Two-storey suburban house at dusk"></div>
  <div class="abs shot" style="left:437px;top:920px;background:linear-gradient(180deg,#5d8fd0,#b9d2ea 40%,#a77a55 60%,#4f9a3a)" role="img" aria-label="Modern villa with wide green lawn"></div>
  <div class="abs shot" style="left:787px;top:920px;background:linear-gradient(180deg,#2f7fd6,#8cc0ee 45%,#f2f2f2 60%,#2f6f7a)" role="img" aria-label="White modernist house under blue sky"></div>
  <a class="abs btn view dark" style="top:1160px" href="#">View More</a>
</section>

<section class="abs testimonials">
  <h2 class="abs section-title">Client Testimonials</h2>

  <div class="abs quote" style="left:216px;top:221px;width:242px;height:194px">Lorem ipsum dolor sit de elit amet, consectetur adipiscing elit. Cras nec libero gravida lacus</div>
  <div class="abs avatar" role="img" aria-label="Client portrait" style="left:297px;top:377px;width:76px;height:76px"></div>
  <div class="abs who" style="left:216px;top:472px;width:242px">Lorem Ipsum<small>Sit Amet</small></div>

  <div class="abs quote" style="left:874px;top:188px;width:242px;height:193px">Lorem ipsum dolor sit de elit amet, consectetur adipiscing elit. Cras nec libero gravida lacus</div>
  <div class="abs avatar" role="img" aria-label="Client portrait" style="left:953px;top:341px;width:76px;height:76px"></div>
  <div class="abs who" style="left:874px;top:439px;width:242px">Lorem Ipsum<small>Sit Amet</small></div>

  <div class="abs quote" style="left:87px;top:537px;width:244px;height:192px">Lorem ipsum dolor sit de elit amet, consectetur adipiscing elit. Cras nec libero gravida lacus</div>
  <div class="abs avatar" role="img" aria-label="Client portrait" style="left:168px;top:691px;width:76px;height:76px"></div>
  <div class="abs who" style="left:87px;top:787px;width:244px">Lorem Ipsum<small>Sit Amet</small></div>

  <div class="abs quote" style="left:744px;top:504px;width:244px;height:191px">Lorem ipsum dolor sit de elit amet, consectetur adipiscing elit. Cras nec libero gravida lacus</div>
  <div class="abs avatar" role="img" aria-label="Client portrait" style="left:827px;top:657px;width:76px;height:76px"></div>
  <div class="abs who" style="left:744px;top:753px;width:244px">Lorem Ipsum<small>Sit Amet</small></div>

  <div class="abs quote main" style="left:433px;top:366px;width:333px;height:248px">Lorem ipsum dolor sit amet, consectetur adipiscing elit. Cras nec libero gravida lacus consectetur sagittis. Integer dapibus libero vel magna volutpat interdum.</div>
  <div class="abs avatar" role="img" aria-label="Featured client portrait" style="left:538px;top:568px;width:122px;height:122px"></div>
  <div class="abs who main" style="left:433px;top:698px;width:333px">LOREM IPSUM<small>SIT AMET</small></div>

  <div class="abs dots"><span></span><span></span><span></span><span></span><span></span></div>
</section>

<footer class="abs footer">
  <div class="abs brand foot"><span class="mark"></span><span>Hollowmere<br>Builders</span></div>

  <div class="abs col" style="left:158px;width:290px">
    <h4>About Us</h4>
    <p>Lorem ipsum is placeholder text commonly used in the graphic, print, and publishing industries.</p>
    <div class="social"><span></span><span></span><span></span><span></span><span></span></div>
  </div>

  <div class="abs col" style="left:541px;width:300px">
    <h4>Contact Us</h4>
    <div class="contact-row" style="font-size:20px"><span class="ic"><svg width="16" height="16" viewBox="0 0 24 24"><path d="M6.6 10.8c1.4 2.8 3.8 5.1 6.6 6.6l2.2-2.2c.3-.3.7-.4 1-.2 1.1.4 2.3.6 3.6.6.6 0 1 .4 1 1V20c0 .6-.4 1-1 1C10.6 21 3 13.4 3 4c0-.6.4-1 1-1h3.5c.6 0 1 .4 1 1 0 1.3.2 2.5.6 3.6.1.3 0 .7-.2 1z" fill="#e31d2f"/></svg></span>0123456789</div>
    <div class="contact-row"><span class="ic"><svg width="16" height="12" viewBox="0 0 28 20"><rect x="1" y="1" width="26" height="18" fill="#e31d2f"/><path d="M1 1 L14 11 L27 1" fill="none" stroke="#fff" stroke-width="2"/></svg></span>info@websitename.com</div>
    <div class="contact-row" style="line-height:18px"><span class="ic"><svg width="14" height="18" viewBox="0 0 14 20"><path d="M7 0C3.1 0 0 3.1 0 7c0 5 7 13 7 13s7-8 7-13c0-3.9-3.1-7-7-7zm0 9.5A2.5 2.5 0 1 1 7 4.5a2.5 2.5 0 0 1 0 5z" fill="#e31d2f"/></svg></span><span>Address line dummy hrere<br>Address line dummy</span></div>
  </div>

  <div class="abs col links" style="left:876px;width:200px">
    <h4>Quick Links</h4>
    <div style="margin-top:12px"><a href="#">About Us</a><a href="#">Services</a><a href="#">Portfolio</a><a href="#">Testimonials</a><a href="#">Contact Us</a></div>
  </div>

  <div class="abs rule"></div>
  <p class="abs copyright">Copyright © 2023 All Rights Reserved By Hollowmere Builders</p>
</footer>

</body>
</html>
```